Veldon Tracing, Inc. - Stationary Project
Business Cards and Stationary for Missing Person Consultants
Professional
Luke Hammond
Search Coordinator
718 West Marlow Avenue
Suite #263
Orlando, FL 32806
lhammond@veldontracing-demo.org
www.VeldonTracing-demo.org
Our organization is called upon
when someone disappears. We¹d like to have a professional business card that
is very eye-catching and people will notice. Please use the red, black and
gray colors in the logo to make a great looking business card, letterhead
and envelope. We look forward to seeing your designs.
We'd like to see a clever use of the logo on the back of the card in bigger format.
This is our logo in AI format.

```html
<!DOCTYPE html>
<html lang="en">
<head>
<meta charset="utf-8">
<title>Veldon Tracing, Inc. – Stationery Set</title>
<link href="https://fonts.googleapis.com/css2?family=Roboto+Condensed:wght@700&family=Open+Sans:wght@400;600&display=swap" rel="stylesheet">
<style>
  :root{
    --red:#c4161c;
    --red-dark:#8e0d12;
    --black:#1d1d1f;
    --charcoal:#3a3a3c;
    --gray:#8a8b8d;
    --light-gray:#d9d9da;
    --watermark:#f1f1f1;
    --paper:#ffffff;
    --backdrop:#e7e4e0;
  }
  *{box-sizing:border-box;margin:0;padding:0}
  html,body{width:1200px;height:530px;overflow:hidden}
  body{background:var(--backdrop);position:relative;font-family:"Open Sans",sans-serif;color:var(--charcoal)}
  .piece{position:absolute;background:var(--paper);box-shadow:0 2px 6px rgba(0,0,0,.25);overflow:hidden}

  /* brand name lockup */
  .brand{display:flex;align-items:center;gap:5px;z-index:1}
  .brand-dot{border-radius:50%;background:var(--red);flex:none}
  .brand-name{font-family:"Roboto Condensed",sans-serif;font-weight:700;text-transform:uppercase;letter-spacing:.5px;line-height:1;color:var(--charcoal);white-space:nowrap}
  .brand.on-dark .brand-name{color:#fff}
  .brand.on-dark .brand-dot{background:#fff}

  /* business cards */
  .card{width:132px;height:72px}
  .card .brand{position:absolute;left:8px;top:9px}
  .card .brand-dot{width:12px;height:12px}
  .card .brand-name{font-size:9px}
  .card-details{position:absolute;left:8px;top:31px;font-size:4.2px;line-height:1.4}
  .card-details .person{font-weight:600;font-size:5px}
  .card-dark{background:var(--charcoal)}
  .card-dark .card-details{color:#ddd}
  .card-back{display:flex;align-items:center;justify-content:center}
  .card-back .brand{position:static;flex-direction:column;gap:5px}
  .card-back .brand-dot{width:20px;height:20px}
  .back-red{background:linear-gradient(135deg,var(--red),var(--red-dark))}
  .back-white{background:var(--paper)}
  .back-black{background:linear-gradient(135deg,var(--charcoal),var(--black))}
  .card-band{position:absolute;left:0;right:0;bottom:0;height:10px;background:var(--red)}

  /* sheets */
  .sheet{width:250px;height:332px;top:40px}
  .sheet-edge{position:absolute;left:0;top:0;bottom:0;width:10px;background:var(--red)}
  .sheet-edge::after{content:"";position:absolute;left:10px;top:0;bottom:0;width:3px;background:var(--black)}
  .sheet .brand{position:absolute;left:24px;top:16px}
  .sheet .brand-dot{width:14px;height:14px}
  .sheet .brand-name{font-size:11px}
  .sheet-contact{position:absolute;top:16px;font-size:4px;line-height:1.4;color:var(--gray);z-index:1}
  .contact-right{right:14px;text-align:right}
  .watermark{position:absolute;left:50%;top:58%;width:140px;height:140px;margin:-70px 0 0 -70px;border-radius:50%;border:12px solid var(--watermark);z-index:0}
  .sheet-footer{position:absolute;left:24px;right:14px;bottom:12px;font-size:4px;color:var(--gray);border-top:1px solid var(--light-gray);padding-top:3px}

  .invoice-title{position:absolute;right:14px;top:44px;font-family:"Roboto Condensed",sans-serif;font-size:10px;color:var(--charcoal)}
  .invoice-meta{position:absolute;left:24px;right:14px;top:60px;display:grid;grid-template-columns:repeat(3,1fr);gap:2px;font-size:3.6px;text-align:center;z-index:1}
  .invoice-meta span{background:var(--light-gray);padding:1px 0}
  .invoice-table{position:absolute;left:24px;top:76px;width:212px;border-collapse:collapse;font-size:3.6px;z-index:1}
  .invoice-table th{background:var(--charcoal);color:#fff;font-weight:600;padding:1.5px;text-align:left}
  .invoice-table td{border-bottom:1px solid var(--light-gray);height:8px}
  .invoice-thanks{position:absolute;left:24px;top:232px;font-size:4px;z-index:1}
  .invoice-totals{position:absolute;right:14px;top:228px;font-size:4px;line-height:1.7;text-align:right;z-index:1}

  .sheet-form .brand{left:auto;right:14px}
  .form-fields{position:absolute;left:24px;right:14px;top:50px;font-size:4.2px;display:grid;grid-template-columns:1fr 1fr;gap:6px 14px;z-index:1}
  .form-fields span{border-bottom:1px solid var(--light-gray);padding-bottom:2px}
  .form-checks{position:absolute;left:24px;right:14px;top:100px;display:flex;justify-content:space-between;font-size:3.8px;z-index:1}
  .form-rule{position:absolute;left:24px;right:14px;top:110px;height:1px;background:var(--light-gray)}

  /* envelopes */
  .envelope-front{left:65px;top:307px;width:228px;height:79px}
  .envelope-front .brand{position:absolute;left:10px;top:10px}
  .envelope-front .brand-dot{width:12px;height:12px}
  .envelope-front .brand-name{font-size:9px}
  .envelope-front .sheet-contact{left:10px;top:28px}
  .envelope-back{top:391px;width:228px;height:96px}
  .envelope-back svg{position:absolute;left:0;top:0;width:100%;height:100%}
  .seal{position:absolute;left:50%;top:32px;width:16px;height:16px;margin-left:-8px;border-radius:50%;background:var(--red);border:2px solid #fff}
</style>
</head>
<body>

<!-- business cards -->
<div class="piece card" style="left:66px;top:43px">
  <div class="brand"><span class="brand-dot"></span><span class="brand-name">Veldon Tracing</span></div>
  <div class="card-details"><div class="person">Luke Hammond</div>Search Coordinator<br>718 West Marlow Avenue, Suite #263<br>lhammond@veldontracing-demo.org</div>
</div>
<div class="piece card card-back back-red" style="left:208px;top:43px">
  <div class="brand on-dark"><span class="brand-dot"></span><span class="brand-name">Veldon Tracing</span></div>
</div>
<div class="piece card card-dark" style="left:66px;top:125px">
  <div class="brand on-dark"><span class="brand-dot" style="background:var(--red)"></span><span class="brand-name">Veldon Tracing</span></div>
  <div class="card-details"><div class="person">Luke Hammond</div>Search Coordinator<br>Orlando, FL 32806<br>www.VeldonTracing-demo.org</div>
  <div class="card-band"></div>
</div>
<div class="piece card card-back back-white" style="left:208px;top:125px">
  <div class="brand"><span class="brand-dot"></span><span class="brand-name">Veldon Tracing</span></div>
</div>
<div class="piece card card-back back-black" style="left:66px;top:209px">
  <div class="brand on-dark"><span class="brand-dot" style="background:var(--red)"></span><span class="brand-name">Veldon Tracing</span></div>
</div>
<div class="piece card card-back back-red" style="left:208px;top:209px">
  <div class="brand on-dark"><span class="brand-dot"></span><span class="brand-name">Veldon Tracing</span></div>
</div>

<!-- envelope front -->
<div class="piece envelope-front">
  <div class="brand"><span class="brand-dot"></span><span class="brand-name">Veldon Tracing</span></div>
  <div class="sheet-contact">718 West Marlow Avenue, Suite #263<br>Orlando, FL 32806</div>
</div>

<!-- letterhead -->
<div class="piece sheet" style="left:376px">
  <div class="watermark"></div>
  <div class="sheet-edge"></div>
  <div class="brand"><span class="brand-dot"></span><span class="brand-name">Veldon Tracing</span></div>
  <div class="sheet-contact contact-right">718 West Marlow Avenue<br>Suite #263<br>Orlando, FL 32806</div>
  <div class="sheet-footer">www.VeldonTracing-demo.org</div>
</div>

<!-- invoice -->
<div class="piece sheet" style="left:632px">
  <div class="watermark" style="top:62%"></div>
  <div class="sheet-edge"></div>
  <div class="brand"><span class="brand-dot"></span><span class="brand-name">Veldon Tracing</span></div>
  <div class="sheet-contact contact-right">718 West Marlow Avenue<br>Suite #263<br>Orlando, FL 32806</div>
  <div class="invoice-title">INVOICE</div>
  <div class="invoice-meta"><span>DATE</span><span>INVOICE NO</span><span>CUSTOMER ID</span></div>
  <table class="invoice-table">
    <thead><tr><th style="width:12%">QTY</th><th style="width:52%">DESCRIPTION</th><th style="width:18%">UNIT PRICE</th><th style="width:18%">AMOUNT</th></tr></thead>
    <tbody>
      <tr><td></td><td></td><td></td><td></td></tr><tr><td></td><td></td><td></td><td></td></tr>
      <tr><td></td><td></td><td></td><td></td></tr><tr><td></td><td></td><td></td><td></td></tr>
      <tr><td></td><td></td><td></td><td></td></tr><tr><td></td><td></td><td></td><td></td></tr>
      <tr><td></td><td></td><td></td><td></td></tr><tr><td></td><td></td><td></td><td></td></tr>
      <tr><td></td><td></td><td></td><td></td></tr><tr><td></td><td></td><td></td><td></td></tr>
      <tr><td></td><td></td><td></td><td></td></tr><tr><td></td><td></td><td></td><td></td></tr>
      <tr><td></td><td></td><td></td><td></td></tr><tr><td></td><td></td><td></td><td></td></tr>
    </tbody>
  </table>
  <div class="invoice-thanks">Thank you for your business!</div>
  <div class="invoice-totals">Sub Total<br>Tax<br>Total</div>
  <div class="sheet-footer">www.VeldonTracing-demo.org</div>
</div>

<!-- fax / form sheet -->
<div class="piece sheet sheet-form" style="left:892px">
  <div class="watermark"></div>
  <div class="brand"><span class="brand-dot"></span><span class="brand-name">Veldon Tracing</span></div>
  <div class="sheet-contact" style="left:24px">718 West Marlow Avenue, Suite #263<br>Orlando, FL 32806</div>
  <div class="form-fields"><span>To:</span><span>From:</span><span>Fax:</span><span>Pages:</span><span>Phone:</span><span>Date:</span><span>Re:</span><span>CC:</span></div>
  <div class="form-checks"><span>□ Urgent</span><span>□ For Review</span><span>□ Please Reply</span><span>□ Recycle</span></div>
  <div class="form-rule"></div>
</div>

<!-- envelope backs -->
<div class="piece envelope-back" style="left:300px">
  <svg viewBox="0 0 228 96" preserveAspectRatio="none"><path d="M0 0H228L114 42Z" fill="var(--black)"/><path d="M0 96L106 46M228 96L122 46" stroke="var(--light-gray)" stroke-width="1"/></svg>
  <div class="seal"></div>
</div>
<div class="piece envelope-back" style="left:542px">
  <svg viewBox="0 0 228 96" preserveAspectRatio="none"><path d="M0 0H228L114 42Z" fill="var(--red)"/><path d="M0 96L106 46M228 96L122 46" stroke="var(--light-gray)" stroke-width="1"/></svg>
  <div class="seal" style="background:var(--charcoal)"></div>
</div>
<div class="piece envelope-back" style="left:787px">
  <svg viewBox="0 0 228 96" preserveAspectRatio="none"><path d="M0 0H228L114 42Z" fill="#f4f4f4" stroke="var(--gray)" stroke-width="1"/><path d="M0 96L106 46M228 96L122 46" stroke="var(--light-gray)" stroke-width="1"/></svg>
  <div class="seal"></div>
</div>

</body>
</html>
```